Business Card Design for Pastor/Church Leadership - simple, elegant, "different"

Design a name card based on logo and color from our branding guide - see file "MBF Logo and Color".
The teal frame around the logo is not part of the logo and is a not necessary design element for the name card (as the attached PDF file may suggest).
The font suggested by branding is "Frutiger 55 Roman".
The file "not good.pdf", a sample of a name card that is NOT good.
- fonts too small to read
- the tagline on the logo "Still waters, open door" not easy to read with logo used in this design
- "MAPLE GROVE FELLOWSHIP" unnecessarily duplicated - possibly because logo too small
- not sure about the green frame, probably better to drop

Target Market(s)

broad, all people the pastor of an international church in Tokyo meets

Industry/Entity Type

Business

Contact Information for Business Card

Mattias R. Pellworth
Pastor
3-9-4 Kawaranodai, Shibuya-ku
Tokyo 150-0048 (Church)
2-21 Ochibamachi, Shibuya-ku
Tokyo 150-0067 (Home)
Tel: 03-5817-2963
E-mail: pastor@maplegrovefell.org
URL: http://www.maplegrovefell.org

Font styles to use
Sans Serif
Other font styles liked:
• Frutiger 55 Roman (want, not must)

Requirements
Must have
• must include logo
• must make use of the "bright turquoise color"
• Cyan = 59, Magenta = 0, Yellow=24, Black=0
• Red=3.1%, Green=91%, Blue=87.1%
• Key Info (name) must be easy to read (see notes on bad sample namecard attached)

```html
<!DOCTYPE html>
<html lang="en">
<head>
<meta charset="utf-8">
<title>Maple Grove Fellowship – Pastor Business Card</title>
<link rel="stylesheet" href="https://fonts.googleapis.com/css2?family=Open+Sans:wght@400;600&family=Arimo:wght@400&display=swap">
<style>
  :root {
    --teal: #62c7ca;
    --paper: #fefefe;
    --backdrop: #f2f2f2;
    --edge: #d6d6d6;
    --white: #ffffff;
  }
  * { margin: 0; padding: 0; box-sizing: border-box; }
  html, body {
    width: 961px;
    height: 1200px;
    overflow: hidden;
    background: var(--backdrop);
  }
  .card {
    position: absolute;
    left: 30px;
    top: 343px;
    width: 900px;
    height: 514px;
    background: var(--paper);
    border: 1px solid var(--edge);
    color: var(--teal);
    font-family: "Open Sans", sans-serif;
    overflow: hidden;
  }
  .card p { position: absolute; line-height: 1; white-space: nowrap; }

  /* brand block */
  .brand-mark {
    position: absolute;
    left: 120px; top: 120px;
    width: 200px;
    text-align: center;
    font-size: 64px;
    font-weight: 600;
    letter-spacing: 4px;
    line-height: 1;
  }
  .brand-name {
    left: 36px; width: 370px; top: 278px;
    text-align: center;
    font-size: 25px;
    letter-spacing: 0.3px;
  }
  .brand-rule {
    position: absolute;
    left: 41px; top: 319px;
    width: 359px; height: 2px;
    background: var(--teal);
  }
  .brand-tagline {
    left: 41px; width: 359px; top: 338px;
    text-align: center;
    font-size: 23px;
    letter-spacing: 0.5px;
  }

  /* contact block */
  .person-name { left: 448px; top: 35px; font-size: 36px; }
  .person-role { left: 448px; top: 86px; font-size: 32px; }
  .address {
    left: 448px;
    font-family: "Arimo", sans-serif;
    font-size: 24px;
  }
  .address .line { display: block; height: 29px; }
  .address-church { top: 146px; }
  .address-home { top: 232px; }
  .phone { left: 448px; top: 305px; font-size: 29px; }
  .email { left: 448px; top: 356px; font-size: 29px; display: flex; align-items: center; gap: 10px; }
  .email svg { width: 26px; height: 18px; margin-top: 6px; }

  /* footer band */
  .web-band {
    position: absolute;
    left: 0; bottom: 0;
    width: 100%; height: 95px;
    background: var(--teal);
    color: var(--white);
    display: flex; align-items: center; justify-content: center;
    font-size: 28px;
    letter-spacing: 0.5px;
  }
</style>
</head>
<body>
  <article class="card">
    <section class="brand">
      <div class="brand-mark">MBF</div>
      <p class="brand-name">MAPLE GROVE FELLOWSHIP</p>
      <div class="brand-rule"></div>
      <p class="brand-tagline">STILL WATERS, OPEN DOOR</p>
    </section>

    <section class="contact">
      <p class="person-name">MATTIAS R. PELLWORTH</p>
      <p class="person-role">PASTOR</p>
      <p class="address address-church">
        <span class="line">3-9-4 KAWARANODAI, SHIBUYA-KU</span>
        <span class="line">TOKYO 150-0048 (CHURCH)</span>
      </p>
      <p class="address address-home">
        <span class="line">2-21 OCHIBAMACHI, SHIBUYA-KU</span>
        <span class="line">TOKYO 150-0067 (HOME)</span>
      </p>
      <p class="phone">Tel: 03-5817-2963</p>
      <p class="email">
        <svg viewBox="0 0 26 18" aria-hidden="true">
          <rect x="0" y="0" width="26" height="18" fill="var(--teal)"/>
          <polyline points="1,1 13,10 25,1" fill="none" stroke="var(--paper)" stroke-width="2"/>
        </svg>
        <span>pastor@maplegrovefell.org</span>
      </p>
    </section>

    <footer class="web-band">WWW.MAPLEGROVEFELL.ORG</footer>
  </article>
</body>
</html>
```